Location services company card

Design a new business card for our location services company. I would like to have the front fairly standard with phone and email, logo, name, title etc. Back should feature text: "Location intelligence: make better decisions with maps." I would like either a location pin on the back to make it obvious that we are involved with maps. This could also have a small mud map on the back (use Vensu.com for design inspiration here).

Target Market(s)

Business and government

Industry/Entity Type

Consultant

Contact Information for Business Card

Name, title, address, phone, mobile, email

Font styles to use
Sans Serif

Requirements
Must have
• Flat design with the company colours:
• C60 M0 Y100 K0 and C100 M20 Y0 K65
• Location pin and/or mud map on back.
• Design must be similar/consistent in feel to tqav.com.au

```html
<!DOCTYPE html>
<html lang="en">
<head>
<meta charset="utf-8">
<title>Tqav business card</title>
<link rel="stylesheet" href="https://fonts.googleapis.com/css2?family=Montserrat:wght@400;600&family=Open+Sans:wght@400;600;700&display=swap">
<style>
  :root {
    --navy: #0c4a6e;
    --green: #6cc04a;
    --white: #ffffff;
    --ink: #1f2a33;
    --rule: #0c4a6e;
    --backdrop: #eceef0;
  }
  * { margin: 0; padding: 0; box-sizing: border-box; }
  html, body { width: 1200px; height: 900px; overflow: hidden; }
  body {
    background: var(--backdrop);
    font-family: "Open Sans", Arial, sans-serif;
    position: relative;
  }
  .card {
    position: absolute;
    left: 280px;
    width: 640px;
    height: 366px;
    overflow: hidden;
    box-shadow: 0 6px 18px rgba(0,0,0,0.12);
  }
  /* back */
  .card-back { top: 67px; background: var(--navy); }
  .map-area { position: absolute; inset: 0; }
  .back-headline {
    position: absolute;
    left: 40px;
    bottom: 36px;
    font-family: "Montserrat", Arial, sans-serif;
  }
  .back-kicker {
    color: var(--white);
    font-weight: 400;
    font-size: 19px;
    letter-spacing: 0.5px;
    text-transform: uppercase;
  }
  .back-title {
    color: var(--green);
    font-weight: 600;
    font-size: 27px;
    letter-spacing: 0.6px;
    text-transform: uppercase;
    margin-top: 2px;
  }
  /* front */
  .card-front { top: 467px; background: var(--white); }
  .brand {
    position: absolute;
    left: 70px;
    top: 128px;
    width: 240px;
  }
  .brand-name {
    display: flex;
    align-items: center;
    gap: 10px;
    font-weight: 700;
    font-size: 44px;
    color: var(--navy);
    line-height: 1;
  }
  .brand-dot {
    width: 14px; height: 14px; border-radius: 50%;
    background: var(--green);
  }
  .divider {
    position: absolute;
    left: 340px; top: 92px;
    width: 1px; height: 118px;
    background: var(--rule);
  }
  .contact { position: absolute; left: 360px; top: 92px; color: var(--ink); }
  .contact-name {
    font-weight: 700; font-size: 17px; text-transform: uppercase;
    color: var(--navy); letter-spacing: 0.3px;
  }
  .contact-name .accent { color: var(--green); }
  .contact-title { font-size: 13px; margin: 2px 0 10px 6px; }
  .contact-list { list-style: none; font-size: 13px; line-height: 21px; margin-left: 6px; }
  .contact-list li { display: flex; align-items: center; gap: 8px; }
  .contact-list svg { width: 10px; height: 10px; fill: var(--navy); flex: none; }
  .band { position: absolute; bottom: 0; height: 24px; }
  .band-navy { left: 0; width: 380px; background: var(--navy); }
  .band-green { left: 380px; right: 0; background: var(--green); }
</style>
</head>
<body>

<section class="card card-back" aria-label="Card back">
  <svg class="map-area" width="640" height="366" viewBox="0 0 640 366">
    <defs>
      <linearGradient id="mapTone" x1="0" y1="0" x2="1" y2="1">
        <stop offset="0" stop-color="#2a6690"/>
        <stop offset="1" stop-color="#1d5a83"/>
      </linearGradient>
    </defs>
    <rect x="20" y="20" width="600" height="230" rx="6" fill="url(#mapTone)" opacity="0.55" role="img" aria-label="World map with office locations"/>
    <g fill="var(--green)">
      <g transform="translate(58 150)"><path d="M0 -14a7 7 0 0 1 7 7c0 5-7 13-7 13s-7-8-7-13a7 7 0 0 1 7-7z"/><circle cy="-7" r="2.6" fill="#0c4a6e"/></g>
      <g transform="translate(205 70)"><path d="M0 -14a7 7 0 0 1 7 7c0 5-7 13-7 13s-7-8-7-13a7 7 0 0 1 7-7z"/><circle cy="-7" r="2.6" fill="#0c4a6e"/></g>
      <g transform="translate(375 75)"><path d="M0 -14a7 7 0 0 1 7 7c0 5-7 13-7 13s-7-8-7-13a7 7 0 0 1 7-7z"/><circle cy="-7" r="2.6" fill="#0c4a6e"/></g>
      <g transform="translate(510 90)"><path d="M0 -14a7 7 0 0 1 7 7c0 5-7 13-7 13s-7-8-7-13a7 7 0 0 1 7-7z"/><circle cy="-7" r="2.6" fill="#0c4a6e"/></g>
      <g transform="translate(180 225)"><path d="M0 -14a7 7 0 0 1 7 7c0 5-7 13-7 13s-7-8-7-13a7 7 0 0 1 7-7z"/><circle cy="-7" r="2.6" fill="#0c4a6e"/></g>
      <g transform="translate(345 215)"><path d="M0 -14a7 7 0 0 1 7 7c0 5-7 13-7 13s-7-8-7-13a7 7 0 0 1 7-7z"/><circle cy="-7" r="2.6" fill="#0c4a6e"/></g>
    </g>
  </svg>
  <div class="back-headline">
    <p class="back-kicker">Location Intelligence:</p>
    <p class="back-title">Make better decisions with maps</p>
  </div>
</section>

<section class="card card-front" aria-label="Card front">
  <div class="brand">
    <p class="brand-name"><span class="brand-dot"></span>tqav</p>
  </div>
  <div class="divider"></div>
  <div class="contact">
    <p class="contact-name">Daniel <span class="accent">Hart</span></p>
    <p class="contact-title">Managing Director</p>
    <ul class="contact-list">
      <li><svg viewBox="0 0 10 10"><path d="M2 0.5l2 2-1 1.2c.6 1.3 1.6 2.3 2.9 2.9l1.2-1 2 2-1.3 1.6C4.6 9 1 5.4.5 1.8z"/></svg>(044)123456789</li>
      <li><svg viewBox="0 0 10 10"><rect y="2" width="10" height="6.5"/><path d="M0 2l5 3.5L10 2" stroke="#fff" stroke-width="0.9" fill="none"/></svg>info@youremail.com</li>
      <li><svg viewBox="0 0 10 10"><circle cx="5" cy="5" r="5"/></svg>www.websitename.com</li>
    </ul>
  </div>
  <div class="band band-navy"></div>
  <div class="band band-green"></div>
</section>

</body>
</html>
```